Fun Billboard

I want a billboard with a fun picture of me (I'm attaching two options)

That will say:

#1 In Real Estate
#1 In Transparency

Warren Pittock

Voted Kelsby's Choice Realtor 2 years in a row!

Call/Text 555-207-4318

Then have my logo and the Kelsby's Choice logo (attached)

and very small across the bottom:

The Lantern Team at Brightmoor Real Estate, 2749 W Tallowden Rd, Bel Air, MD 20987 555-341-9062

Billboard size is 14' tall by 48' wide

```html
<!DOCTYPE html>
<html lang="en">
<head>
<meta charset="utf-8">
<title>Warren Pittock Billboard</title>
<link rel="stylesheet" href="https://fonts.googleapis.com/css2?family=Poppins:wght@600;700;800&family=Bebas+Neue&display=swap">
<style>
  :root{
    --navy:#0a2a66;
    --navy-deep:#061f52;
    --orange:#ef7d2e;
    --orange-light:#f5943f;
    --white:#ffffff;
    --stage:#b5b5b5;
    --badge:#2b2623;
    --photo-a:#2a2d38;
    --photo-b:#e79bb0;
  }
  html,body{margin:0;padding:0;overflow:hidden}
  body{width:1121px;height:1200px;background:var(--stage);position:relative}
  .billboard{
    position:absolute;left:40px;top:448px;width:1040px;height:303px;
    background:var(--white);overflow:hidden;
    box-shadow:0 4px 12px rgba(0,0,0,.25);
  }
  .billboard svg.backdrop{position:absolute;inset:0}
  .headline-number{
    position:absolute;left:24px;top:14px;margin:0;
    font:800 92px/1 "Poppins",sans-serif;color:var(--white);letter-spacing:-3px;
  }
  .headline-lines{position:absolute;left:146px;top:18px;margin:0}
  .headline-lines span{display:block;font:700 45px/42px "Poppins",sans-serif;white-space:nowrap}
  .headline-lines .accent{color:var(--orange)}
  .headline-lines .plain{color:var(--white)}
  .phone-number{
    position:absolute;left:93px;top:119px;
    font:700 54px/1 "Poppins",sans-serif;color:var(--white);letter-spacing:1px;white-space:nowrap;
  }
  .team-mark{position:absolute;left:28px;top:204px;width:130px;text-align:center}
  .team-mark .dot{width:26px;height:26px;border-radius:50%;background:var(--navy);margin:0 auto 8px}
  .team-mark .name{font:700 15px/1.15 "Poppins",sans-serif;color:var(--navy)}
  .award-badge{position:absolute;left:181px;top:186px;width:98px;height:98px;border-radius:50%;background:var(--badge)}
  .agent-name{
    position:absolute;left:315px;top:192px;margin:0;
    font:400 56px/1 "Bebas Neue",sans-serif;color:var(--navy);letter-spacing:1px;white-space:nowrap;
  }
  .agent-address{
    position:absolute;left:317px;top:248px;width:296px;margin:0;
    font:600 10px/14px "Poppins",sans-serif;color:var(--navy-deep);
  }
  .agent-address svg{vertical-align:-1px;margin-right:4px}
  .agent-photo{
    position:absolute;left:625px;top:22px;width:160px;height:281px;
    background:linear-gradient(180deg,var(--photo-a) 0%,var(--photo-a) 62%,var(--photo-b) 100%);
    border-radius:40px 40px 0 0;
  }
  .award-copy{position:absolute;left:800px;top:38px;width:248px;text-align:center}
  .award-copy .voted{font:700 30px/30px "Poppins",sans-serif;color:var(--white);margin:0}
  .award-copy .streak{font:400 62px/56px "Bebas Neue",sans-serif;color:var(--navy-deep);margin:14px 0 0}
</style>
</head>
<body>
  <section class="billboard">
    <svg class="backdrop" width="1040" height="303" viewBox="0 0 1040 303" aria-hidden="true">
      <defs>
        <linearGradient id="skyBlue" x1="0" x2="1" y1="0" y2="0">
          <stop offset="0" stop-color="#062a6e"/>
          <stop offset="0.6" stop-color="#0d3f98"/>
          <stop offset="1" stop-color="#1a5fc8"/>
        </linearGradient>
      </defs>
      <polygon points="0,0 840,0 840,172 0,168" fill="url(#skyBlue)"/>
      <polygon points="22,118 640,116 640,178 24,184" fill="var(--orange)"/>
      <circle cx="57" cy="150" r="25" fill="var(--navy)"/>
      <path d="M48 140c2-2 4-2 5 0l3 5c1 2 0 3-1 4l-2 2c1 3 4 6 7 7l2-2c1-1 2-2 4-1l5 3c2 1 2 3 0 5l-2 2c-3 3-10 1-17-6s-9-14-6-17z" fill="var(--white)"/>
    </svg>

    <h1 class="headline-number">#1</h1>
    <p class="headline-lines">
      <span class="accent">IN REAL ESTATE</span>
      <span class="plain">IN TRANSPARENCY</span>
    </p>
    <div class="phone-number">555-207-4318</div>

    <div class="team-mark">
      <div class="dot"></div>
      <div class="name">The Lantern Team</div>
    </div>
    <div class="award-badge" aria-hidden="true"></div>

    <h2 class="agent-name">WARREN PITTOCK</h2>
    <p class="agent-address"><svg width="7" height="10" viewBox="0 0 7 10"><path d="M3.5 0A3.5 3.5 0 0 0 0 3.5C0 6 3.5 10 3.5 10S7 6 7 3.5A3.5 3.5 0 0 0 3.5 0zm0 5A1.5 1.5 0 1 1 3.5 2a1.5 1.5 0 0 1 0 3z" fill="currentColor"/></svg>The Lantern Team at Brightmoor Real Estate, 2749 W Tallowden Rd, Bel Air, MD 20987 555-341-9062</p>

    <div class="agent-photo" role="img" aria-label="Photo of the realtor in a dark suit with arms spread, wearing a pink flamingo pool float"></div>

    <svg class="backdrop" width="1040" height="303" viewBox="0 0 1040 303" aria-hidden="true">
      <polygon points="836,0 1040,0 1040,303 781,303 786,284 779,268 790,250 782,232 792,214 784,196 796,178 788,160 800,142 793,124 806,106 798,88 812,70 806,52 822,34 815,16" fill="var(--orange-light)"/>
    </svg>

    <div class="award-copy">
      <p class="voted">VOTED<br>KELSBY'S<br>CHOICE<br>REALTOR</p>
      <p class="streak">2 YEARS<br>IN A ROW!</p>
    </div>
  </section>
</body>
</html>
```